Webdesign für Helga Stirnweis, Corvell Management
Zielgruppe
Unternehmensberatung, Schwerpunkt Leadership development, Personalentwicklung und -beratung, Karrierecoaching, es soll auf jeder Seite auch ein link sein zur Englischseite;
ungefährer startseitetext: Mein Ziel: Begeistern und Befähigen;
Lernen und Veränderungen entstehen aus Reflexion. Der Betreffende tritt einen Schritt zurück, schaut auf das bisherige Verhalten und stellt sich die Frage, ob er dieses Verhalten und die Auswirkungen dieses Verhaltens in Zukunft wieder wählen möchten.
Leadership
• Fähigkeiten bei ihren MitarbeiterInnen aktivieren, welche sie sich selbst vielleicht nicht zugetraut hätten.
• Die Vielfalt unter ihren MitarabeiterInnen schätzen und die Unterschiede als Ressourcen nutzen.
• Eine Organisation schaffen, der ihre MitarbeiterInnen gerne angehören und in die sie gerne aktiv ihre Kompetenzen und ihr Potenzial einbringen.
Coaching:
Mein Ziel ist, Sie in ihren Herausforderung und Veränderungen zu unterstützen. Bei Veränderungen in ihrem beruflichen Werdegang oder den täglichen Herausforderungen, z.B. mit dem Zeitmanagement, werde ich Sie begleiten und beharrlich fordern.
Aufgabenstellung
es sollen Fotos (trainingsituationen) integriert werden, Schrift Geneva und Avenir Next gefallen mir, Logo vorhanden - in Farbe nachtblau/nightblue und schwarz;
gute Freunde beschreiben mich als: gewissenhaft, integrierend, beharrlich, ausdrucksstark, vertrauensvoll, offen, durchgreifend;

```html
<!DOCTYPE html>
<html lang="de">
<head>
<meta charset="utf-8">
<title>Corvell Management – Helga Stirnweis</title>
<link href="https://fonts.googleapis.com/css2?family=Montserrat:wght@400;500;600;700&family=Lora:ital@1&display=swap" rel="stylesheet">
<style>
:root{
  --night:#3b3785;
  --ink:#111118;
  --text:#6b6b73;
  --muted:#8a8a92;
  --line:#dcdce2;
  --band:#f4f4f4;
  --white:#ffffff;
}
*{box-sizing:border-box;margin:0;padding:0}
html,body{width:1200px;height:2996px;overflow:hidden;background:var(--white)}
body{font-family:'Montserrat',sans-serif;color:var(--text);position:relative}
.abs{position:absolute}
/* header */
.logo{left:106px;top:24px;color:var(--night);font-weight:600;font-size:26px;letter-spacing:.5px;line-height:1}
.logo small{display:block;font-size:11px;font-weight:500;letter-spacing:2px;margin-top:4px;text-transform:uppercase}
.contact-top{top:32px;display:flex;align-items:center;gap:10px;font-size:12px;color:var(--ink);font-weight:500;line-height:1.25}
.contact-top.addr{left:776px}
.contact-top.tel{left:920px;font-size:15px}
.navbar{top:83px;left:0;width:1200px;height:41px;background:var(--night)}
.navbar ul{list-style:none;display:flex;position:absolute;left:136px;top:0;height:41px;align-items:center}
.navbar li{color:var(--white);font-size:14px;font-weight:600;letter-spacing:1.6px;margin-right:62px}
.search{left:1067px;top:93px;width:24px;height:24px;border-radius:50%;background:#6f6caa}
/* hero */
.hero{top:124px;left:0;width:1200px;height:383px;background:linear-gradient(90deg,#8a8f9a 0%,#e9e9ea 30%,#f2f2f2 55%,#b9aca4 80%,#6e5a52 100%)}
.hero-title{left:405px;top:241px;width:386px;height:76px;background:var(--white);color:var(--ink);font-weight:700;font-size:50px;letter-spacing:7px;text-align:center;line-height:80px}
.hero-sub{left:347px;top:317px;width:502px;height:56px;background:var(--white);color:var(--ink);font-weight:600;font-size:25px;letter-spacing:4px;text-align:center;line-height:58px}
/* welcome */
.photo{background:linear-gradient(160deg,#e9e7e3,#a88a6c 55%,#4e3a2c)}
.welcome-img{left:106px;top:575px;width:422px;height:269px}
.kicker{font-family:'Lora',serif;font-style:italic;font-size:12px;color:var(--text)}
.welcome-kicker{left:612px;top:573px}
.welcome-h{left:612px;top:604px;font-size:20px;font-weight:600;letter-spacing:3.4px;color:var(--ink)}
.welcome-p{left:612px;top:647px;width:480px;font-size:12.5px;line-height:25.5px}
.btn{background:var(--night);color:var(--white);font-weight:600;font-size:12px;letter-spacing:1px;text-align:center;text-transform:uppercase}
.welcome-btn{left:612px;top:771px;width:253px;height:42px;line-height:42px}
/* services */
.band{left:0;width:1200px;background:var(--band)}
.services-band{top:911px;height:445px}
.section-h{left:0;width:1200px;text-align:center;color:var(--ink);font-weight:600;font-size:33px;letter-spacing:-.6px}
.service{width:220px;text-align:center;top:1048px}
.service .ico{width:86px;height:86px;border-radius:50%;background:var(--white);border:1px solid var(--line);margin:0 auto;display:flex;align-items:center;justify-content:center}
.service h3{margin-top:36px;font-size:10.5px;font-weight:600;letter-spacing:1px;color:var(--ink)}
.service p{margin-top:11px;font-size:12.5px;line-height:20px}
.service .btn{width:119px;height:33px;line-height:33px;margin:21px auto 0;font-size:11px}
/* testimonials */
.quote-card{top:1505px;width:428px;height:230px;border:1px solid var(--line);background:var(--white)}
.avatar{width:96px;height:96px;border-radius:50%;background:linear-gradient(180deg,#d8c8bd,#8b7468)}
.quote{width:330px;font-family:'Lora',serif;font-style:italic;font-size:11.5px;line-height:25.5px;color:var(--text)}
.who{font-size:10.5px;font-weight:500;color:var(--ink);letter-spacing:.3px}
.role{font-family:'Lora',serif;font-style:italic;font-size:10.5px;color:var(--muted)}
.divider{top:1803px;left:0;width:1200px;height:1px;background:var(--line)}
/* blog */
.post-img{top:1939px;width:313px;height:218px}
.date{width:49px;height:42px;background:var(--night);color:var(--white);font-size:13px;font-weight:600;text-align:center;line-height:16px;padding-top:5px;top:2083px}
.post-h{top:2180px;font-size:17px;font-weight:600;color:var(--ink);letter-spacing:.4px}
.post-p{top:2215px;width:313px;font-size:11px;line-height:20px}
.more{top:2292px;font-size:10.5px;font-weight:600;color:var(--ink);display:flex;align-items:center;gap:8px}
/* contact */
.contact-band{top:2362px;height:481px}
.contact-h{left:105px;top:2407px;font-size:30px;font-weight:600;color:var(--ink)}
.contact-intro{left:105px;top:2464px;width:460px;font-family:'Lora',serif;font-style:italic;font-size:14px;line-height:21px;color:var(--text)}
.field{left:105px;width:451px;background:var(--white);font-family:'Lora',serif;font-style:italic;font-size:10px;letter-spacing:.8px;color:var(--ink);padding:11px 13px;text-transform:uppercase}
.field em{color:#d33;font-style:normal;margin-right:3px}
.send{left:421px;top:2757px;width:135px;height:33px;border:2px solid #9e9ea6;font-size:11px;font-weight:500;letter-spacing:2.5px;color:var(--ink);text-align:center;line-height:29px;background:var(--white)}
.touch-h{left:671px;top:2468px;font-size:20px;font-weight:600;color:var(--ink);letter-spacing:.8px}
.touch-row{left:671px;display:flex;gap:20px;font-size:11px;color:var(--text);line-height:13px;letter-spacing:.3px}
.social{top:2658px;width:36px;height:36px;border-radius:50%;background:var(--white);border:1px solid var(--line)}
.social.on{background:var(--night);border-color:var(--night)}
/* footer */
.footer{top:2843px;left:0;width:1200px;height:153px;background:var(--night)}
.footer ul{list-style:none;position:absolute;left:0;width:1200px;top:50px;display:flex;justify-content:center;gap:62px}
.footer li{color:var(--white);font-size:13px;font-weight:600;letter-spacing:1.6px}
.copy{position:absolute;left:0;width:1200px;top:90px;text-align:center;color:var(--white);font-size:10px;font-weight:600;letter-spacing:1px}
</style>
</head>
<body>

<header>
  <div class="abs logo">Corvell<small>Management</small></div>
  <div class="abs contact-top addr">
    <svg width="14" height="20" viewBox="0 0 14 20"><path d="M7 0a7 7 0 0 0-7 7c0 5 7 13 7 13s7-8 7-13a7 7 0 0 0-7-7z" fill="#111"/><circle cx="7" cy="7" r="2.6" fill="#fff"/></svg>
    <span>Lindenweg 14<br>40210 Feldhausen</span>
  </div>
  <div class="abs contact-top tel">
    <svg width="13" height="20" viewBox="0 0 13 20"><rect x="1" y="1" width="11" height="18" rx="2" fill="none" stroke="#111" stroke-width="2"/><circle cx="6.5" cy="15.5" r="1.2" fill="#111"/></svg>
    <span style="color:#2a2a1a">+49 (0)2100 5550147</span>
  </div>
  <nav class="abs navbar">
    <ul><li>HOME</li><li>ABOUT US</li><li>SERVICES <svg width="8" height="5" viewBox="0 0 8 5"><path d="M1 1l3 3 3-3" stroke="#fff" fill="none"/></svg></li><li>GOAL</li><li>CONTACT</li></ul>
  </nav>
  <div class="abs search"><svg width="24" height="24" viewBox="0 0 24 24"><circle cx="11" cy="11" r="3.6" fill="none" stroke="#fff" stroke-width="1.6"/><path d="M13.6 13.6l2.6 2.6" stroke="#fff" stroke-width="1.8"/></svg></div>
</header>

<section class="abs hero" role="img" aria-label="Foto: Trainerin präsentiert vor aufmerksamen Seminarteilnehmern"></section>
<div class="abs hero-title">MEIN ZIEL:</div>
<div class="abs hero-sub">BEGEISTERN UND BEFÄHIGEN</div>

<section>
  <div class="abs photo welcome-img" role="img" aria-label="Foto: Seminarraum mit Publikum von hinten, Vortragender vorne"></div>
  <p class="abs kicker welcome-kicker">Welcome to Helga Stirnweis, Corvell Management</p>
  <h2 class="abs welcome-h">GROWTH UP YOUR BUSINESS</h2>
  <p class="abs welcome-p">There are many variations of passages of Lorem Ipsum available, but the majority have suffered alteration in some form, by injected humour, or randomised words which don't look even slightly believable. If you are going to use a passage of Lorem Ipsum, you need to be sure .</p>
  <div class="abs btn welcome-btn">Learn More</div>
</section>

<section>
  <div class="abs band services-band"></div>
  <h2 class="abs section-h" style="top:972px">Our Services</h2>
  <div class="abs service" style="left:109px">
    <div class="ico"><svg width="40" height="32" viewBox="0 0 40 32"><rect x="14" y="1" width="12" height="6" rx="1" fill="none" stroke="#111" stroke-width="2.5"/><rect x="1" y="6" width="38" height="25" rx="3" fill="#111"/><rect x="4" y="14" width="32" height="2" fill="#fff"/></svg></div>
    <h3>BUSINESS CONSULTANCY</h3><p>Lorem ipsum dolor sit amet,<br>consectetuer adipiscing elit,</p><div class="btn">Learn More</div>
  </div>
  <div class="abs service" style="left:361px">
    <div class="ico"><svg width="42" height="40" viewBox="0 0 42 40"><rect x="1" y="1" width="40" height="28" fill="none" stroke="#111" stroke-width="2.5"/><path d="M1 7h40" stroke="#111" stroke-width="2.5"/><circle cx="20" cy="28" r="8" fill="#111"/><circle cx="20" cy="28" r="3" fill="#fff"/><path d="M20 17v4M20 35v4M9 28h4M27 28h4" stroke="#111" stroke-width="3"/></svg></div>
    <h3>LEADERSHIP DEVELOPMENT</h3><p>Lorem ipsum dolor sit amet,<br>consectetuer adipiscing elit,</p><div class="btn">Learn More</div>
  </div>
  <div class="abs service" style="left:617px">
    <div class="ico"><svg width="34" height="38" viewBox="0 0 34 38"><circle cx="17" cy="11" r="9" fill="#111"/><path d="M1 38c0-10 7-16 16-16s16 6 16 16z" fill="#111"/><path d="M17 22l-2 4 2 9 2-9z" fill="#fff"/></svg></div>
    <h3>STAFF DEVELOPMENT &amp; CONSULTING</h3><p>Lorem ipsum dolor sit amet,<br>consectetuer adipiscing elit,</p><div class="btn">Learn More</div>
  </div>
  <div class="abs service" style="left:869px">
    <div class="ico"><svg width="46" height="40" viewBox="0 0 46 40"><rect x="18" y="2" width="26" height="18" fill="none" stroke="#111" stroke-width="2.5"/><circle cx="36" cy="11" r="3.5" fill="none" stroke="#111" stroke-width="2"/><circle cx="8" cy="8" r="4.5" fill="#111"/><path d="M3 15h11l10-4v3l-9 5v21h-4V30H8v10H4z" fill="#111"/></svg></div>
    <h3>CAREER COACHING</h3><p>Lorem ipsum dolor sit amet,<br>consectetuer adipiscing elit,</p><div class="btn">Learn More</div>
  </div>
</section>

<section>
  <h2 class="abs section-h" style="top:1415px">What they said?</h2>
  <div class="abs quote-card" style="left:158px"></div>
  <div class="abs avatar" style="left:104px;top:1554px" role="img" aria-label="Porträtfoto einer Kundin"></div>
  <p class="abs quote" style="left:235px;top:1536px">"“Sed ut perspiciatis unde omnis iste natus error sit voluptatem accusantium doloremque laudantium, totam rem aperiam, eaque ipsa quae ab illo inventore veritatis et quasi architecto beatae vitae dicta sunt explicabo. ”</p>
  <p class="abs who" style="left:235px;top:1665px">TOBIAS RENNER</p>
  <p class="abs role" style="left:235px;top:1682px">CEO/ Founder Norlan Systems</p>

  <div class="abs quote-card" style="left:665px"></div>
  <div class="abs avatar" style="left:612px;top:1554px" role="img" aria-label="Porträtfoto eines Kunden"></div>
  <p class="abs quote" style="left:743px;top:1536px">"“Sed ut perspiciatis unde omnis iste natus error sit voluptatem accusantium doloremque laudantium, totam rem aperiam, eaque ipsa quae ab illo inventore veritatis et quasi architecto beatae vitae dicta sunt explicabo. ”</p>
  <p class="abs who" style="left:743px;top:1665px">CLARA VOSS</p>
  <p class="abs role" style="left:743px;top:1682px">CEO/ Founder Velbrook Group</p>
</section>
<div class="abs divider"></div>

<section>
  <h2 class="abs section-h" style="top:1862px;letter-spacing:.6px">Latest Blog</h2>

  <div class="abs photo post-img" style="left:106px;background:linear-gradient(180deg,#f1f1ef,#d9d9d7 55%,#6e6e78)" role="img" aria-label="Foto: Präsentation vor Leinwand im Besprechungsraum"></div>
  <div class="abs date" style="left:106px">08<br>JUN</div>
  <h3 class="abs post-h" style="left:106px">Brooklyn</h3>
  <p class="abs post-p" style="left:106px">Sed ut perspiciatis unde omnis iste natus error sit voluptatem accusantium doloremque laudantium, totam rem aperiam.</p>
  <div class="abs more" style="left:346px">Read More <svg width="6" height="9" viewBox="0 0 6 9"><path d="M1 1l3.5 3.5L1 8" stroke="#111" fill="none" stroke-width="1.3"/></svg></div>

  <div class="abs photo post-img" style="left:443px;background:linear-gradient(160deg,#cdd3d8,#d8c24a 55%,#2c3d6c)" role="img" aria-label="Foto: applaudierende Seminarteilnehmer"></div>
  <div class="abs date" style="left:443px">07<br>JUN</div>
  <h3 class="abs post-h" style="left:443px">Harbor Juicery</h3>
  <p class="abs post-p" style="left:443px">On the other hand, we denounce with righteous indignation and dislike men who are so beguiled and demoralized</p>
  <div class="abs more" style="left:685px">Read More <svg width="6" height="9" viewBox="0 0 6 9"><path d="M1 1l3.5 3.5L1 8" stroke="#111" fill="none" stroke-width="1.3"/></svg></div>

  <div class="abs photo post-img" style="left:781px;background:linear-gradient(180deg,#f2f2f2,#b4b4b6 45%,#3e4b60)" role="img" aria-label="Foto: Mikrofon vor unscharfem Publikum"></div>
  <div class="abs date" style="left:781px">06<br>JUN</div>
  <h3 class="abs post-h" style="left:781px">Hello Riverside Project</h3>
  <p class="abs post-p" style="left:781px">Lorem ipsum dolor sit amet, consectetur adipiscing elit, sed do eiusmod tempor incididunt ut labore et dolore magna aliqua. Ut enim ad minim veniam,</p>
  <div class="abs more" style="left:1023px">Read More <svg width="6" height="9" viewBox="0 0 6 9"><path d="M1 1l3.5 3.5L1 8" stroke="#111" fill="none" stroke-width="1.3"/></svg></div>
</section>

<section>
  <div class="abs band contact-band"></div>
  <h2 class="abs contact-h">Contact us</h2>
  <p class="abs contact-intro">Please don't hesitate to contact me if you have any questions, commnets or messages. I'll try to respond to everything!</p>
  <div class="abs field" style="top:2533px;height:34px"><em>*</em>Name</div>
  <div class="abs field" style="top:2584px;height:34px"><em>*</em>Email</div>
  <div class="abs field" style="top:2635px;height:105px">Message</div>
  <div class="abs send">SEND ME</div>

  <h3 class="abs touch-h">Get in touch</h3>
  <div class="abs touch-row" style="top:2523px">
    <svg width="18" height="16" viewBox="0 0 18 16"><path d="M1 8L9 1l8 7M3 6v9h12V6M7 15v-5h4v5" fill="none" stroke="#888" stroke-width="1.2"/></svg>
    <span>48 Sample Lane, Harbor House,<br>Westfield, Exampleland.</span>
  </div>
  <div class="abs touch-row" style="top:2560px">
    <svg width="18" height="15" viewBox="0 0 18 15"><rect x="5" y="1" width="8" height="13" rx="1" fill="none" stroke="#888" stroke-width="1.2"/></svg>
    <span>(0049) 5550 1234 000</span>
  </div>
  <div class="abs touch-row" style="top:2588px">
    <svg width="18" height="13" viewBox="0 0 18 13"><rect x="1" y="1" width="16" height="11" fill="none" stroke="#888" stroke-width="1.2"/><path d="M1 1l8 6 8-6" fill="none" stroke="#888" stroke-width="1.2"/></svg>
    <span>hello@corvell-example.com</span>
  </div>
  <div class="abs social" style="left:672px"></div>
  <div class="abs social on" style="left:715px"></div>
  <div class="abs social" style="left:759px"></div>
  <div class="abs social" style="left:803px"></div>
  <div class="abs social" style="left:847px"></div>
  <div class="abs social" style="left:891px"></div>
</section>

<footer class="abs footer">
  <ul><li>HOME</li><li>ABOUT US</li><li>SERVICES</li><li>GOAL</li><li>CONTACT</li></ul>
  <p class="copy">© 2016 CORVELL MANAGEMENT. POWERED BY WEBFORGE</p>
</footer>

</body>
</html>
```